Business Cards that are elegant and wow

I want to create and print business cards that represent my brand and stand out from the rest. We want to ensure they stay in our branding and the integrity is not lost. I am happy to look at different shapes like square etc.

It will be printed on very thick cards and will be stylish .

I want to create and print business cards that represent my brand and stand out from the rest. We want to ensure they stay in ur branding and the integrity is not lost. I am happy to look at different shapes like square etc.

Target Market(s)

real estate professionals

Industry/Entity Type

Real Estate

Contact Information for Business Card

Maren Holt
hello@brightfernrealty.com.au
brightfernrealty.com.au
0487 316 252 (SMS)

Colors

Designer to choose colors to be used in the design.

Requirements
Must have
• My logo
• email
• website
• Name
Nice to have
• I like the idea of printing with foil or spot gloss. You want it to stand out in a sea.
Should not have
• I would like you to stay in my colour themes. Don't change the colour of my logo

```html
<!DOCTYPE html>
<html lang="en">
<head>
<meta charset="utf-8">
<title>Bright Fern Realty – Business Card</title>
<link href="https://fonts.googleapis.com/css2?family=Montserrat:wght@600;700&family=Lato:wght@400&display=swap" rel="stylesheet">
<style>
  :root {
    --brand-blue: #00aeef;
    --brand-pink: #e6127d;
    --card-white: #ffffff;
    --backdrop: #ecebe9;
  }
  html, body {
    margin: 0;
    width: 1200px;
    height: 900px;
    overflow: hidden;
    background: var(--backdrop);
  }
  .business-card {
    position: absolute;
    left: 115px;
    top: 150px;
    width: 970px;
    height: 602px;
    background: var(--card-white);
    box-shadow: 0 6px 24px rgba(0,0,0,0.12);
    overflow: hidden;
  }
  .brand-mark {
    position: absolute;
    left: 75px;
    top: 88px;
    width: 142px;
    height: 142px;
  }
  .brand-divider {
    position: absolute;
    left: 231px;
    top: 82px;
    width: 3px;
    height: 156px;
    background: var(--brand-pink);
  }
  .brand-name {
    position: absolute;
    left: 250px;
    top: 100px;
    margin: 0;
    font-family: "Montserrat", sans-serif;
    font-weight: 700;
    color: var(--brand-blue);
    line-height: 1;
  }
  .brand-name .line-main {
    display: block;
    font-size: 62px;
    letter-spacing: 0.01em;
  }
  .brand-name .line-sub {
    display: block;
    margin-top: 18px;
    font-size: 38px;
    letter-spacing: 0.52em;
  }
  .agent-name {
    position: absolute;
    left: 232px;
    top: 327px;
    margin: 0;
    padding-left: 24px;
    border-left: 3px solid var(--brand-blue);
    font-family: "Montserrat", sans-serif;
    font-weight: 700;
    font-size: 38px;
    line-height: 42px;
    color: var(--brand-blue);
  }
  .contact-list {
    position: absolute;
    left: 232px;
    top: 400px;
    margin: 0;
    padding: 0 0 0 24px;
    list-style: none;
    border-left: 3px solid var(--brand-pink);
    font-family: "Lato", sans-serif;
    font-size: 25px;
    color: var(--brand-pink);
  }
  .contact-list li {
    display: flex;
    align-items: center;
    height: 35.5px;
  }
  .contact-icon {
    width: 20px;
    height: 20px;
    margin-right: 8px;
    fill: var(--brand-pink);
    flex: none;
  }
  .accent-bar {
    position: absolute;
    left: 0;
    bottom: 0;
    width: 100%;
    height: 28px;
    display: flex;
  }
  .accent-bar .accent-pink { width: 232px; background: var(--brand-pink); }
  .accent-bar .accent-blue { flex: 1; background: var(--brand-blue); }
</style>
</head>
<body>
  <div class="business-card">
    <svg class="brand-mark" viewBox="0 0 142 142" aria-hidden="true">
      <circle cx="71" cy="71" r="65" fill="none" stroke="#00aeef" stroke-width="9"/>
    </svg>
    <div class="brand-divider"></div>
    <h1 class="brand-name">
      <span class="line-main">BRIGHT FERN</span>
      <span class="line-sub">REALTY</span>
    </h1>

    <h2 class="agent-name">MAREN HOLT</h2>

    <ul class="contact-list">
      <li>
        <svg class="contact-icon" viewBox="0 0 20 20" aria-hidden="true"><path d="M4 5c2-2 10-2 12 0l1 3h-4l-1-2H8L7 8H3zM5 9h10l2 7H3z"/></svg>
        0487 316 252
      </li>
      <li>
        <svg class="contact-icon" viewBox="0 0 20 20" aria-hidden="true"><path d="M2 5h16v11H2zM3 6l7 5 7-5v1.5l-7 5-7-5z" fill-rule="evenodd"/></svg>
        hello@brightfernrealty.com.au
      </li>
      <li>
        <svg class="contact-icon" viewBox="0 0 20 20" aria-hidden="true"><circle cx="10" cy="10" r="8"/><path d="M6 6c2 1 3 3 2 5s-2 2-1 5M12 4c-1 2 0 3 2 3s2 3 1 5" stroke="#fff" stroke-width="1.5" fill="none"/></svg>
        www.brightfernrealty.com.au
      </li>
    </ul>

    <div class="accent-bar">
      <div class="accent-pink"></div>
      <div class="accent-blue"></div>
    </div>
  </div>
</body>
</html>
```